We Buy Houses Website

Looking for a highly motivated and skillfull designer to design and code me a "we Buy Houses" type website. I have a potential logo, but if you think you can make a BETTER one, please do try and incorporate it in your template. I am looking for creativity, professionalism, simple yet elegant. I will need a simple form on the front of the template along with pictures I provide you of recent houses I have bought. Look at these sites for examples of the layout of the website:

http://www.brickwaleholdings.example/
http://www.marlowtakesplots.example/
http://www.quickdwellingexit.example/

If you make me a design that blows me away, and you are dependable, you will become part of my team and in charge of the web aspect which will include designing, updating, any and all graphics and logo work, SEO, coding. If you have skills in all of these areas please make me a design and lets do business!! The name of the website will be "Tovin Takes Homes" at TovinTakesHomes.example

I have uploaded some pictures of houses that we have done, please feel free to incorporate this into the banner or the design, etc. I want them to know we buy houses in ANY condition, as is, cash, can close immediately so they can get on with their life. We have many options to help them find a solution to whatever problem they have. We are in the business of helping people.

Target Market(s)

People looking to sell their houses
people facing foreclosure, bankruptcy, death in the family, divorce, anyone that we can help
people with ugly houses that need a lot of repair

Industry/Entity Type

Business

Font styles to use
Serif
Sans Serif

Colors

Designer to choose colors to be used in the design.

Requirements
Must have
• must have a simple form on the front of the page, preferrably near the banner, with the few required fields to help someone get started putting in their interest to sell their house, view the 2 websites i put as examples to see what kind of fields it should have.

My phone number (555) 481-7720 along with a Tovin Takes Homes logo, clean simple and elegant and professional. I want a nice color scheme that is not white but professional and has a wow factor.

```html
<!DOCTYPE html>
<html lang="en">
<head>
<meta charset="utf-8">
<title>Tovin Takes Homes</title>
<link rel="stylesheet" href="https://fonts.googleapis.com/css2?family=Source+Sans+3:wght@300;400;600;700&display=swap">
<style>
:root{
  --sky:#5cb9ef;
  --sky-dark:#3a9fdc;
  --slate:#3d4b58;
  --slate-deep:#2c3945;
  --footer:#4b5b67;
  --footer-line:#6a7984;
  --ink:#3f4750;
  --muted:#6b737b;
  --white:#ffffff;
  --field:#eef1f4;
}
*{box-sizing:border-box;margin:0;padding:0}
html,body{width:1200px;height:3340px;overflow:hidden}
body{font-family:"Source Sans 3",Arial,sans-serif;color:var(--ink);background:var(--white);position:relative}
.abs{position:absolute}

/* header */
.site-header{top:0;left:0;width:1200px;height:120px;background:var(--white);border-top:6px solid var(--sky)}
.brand{left:160px;top:52px;display:flex;align-items:center;gap:10px}
.brand-square{width:26px;height:26px;background:var(--sky)}
.brand-name{font-weight:700;font-size:20px;color:var(--slate);letter-spacing:.5px}
.topbar-phone{left:478px;top:4px;display:flex;align-items:center;gap:8px;font-size:15px;color:var(--muted)}
.phone-badge{width:32px;height:32px;background:var(--sky);border-radius:3px;display:flex;align-items:center;justify-content:center}
.social{display:flex;gap:8px}
.social span{width:22px;height:22px;border-radius:50%;background:#8a929a;display:block}
.topbar-social{left:660px;top:11px}
.btn-signup{left:873px;top:11px;width:73px;height:29px;background:var(--sky);color:var(--white);font-size:14px;text-align:center;line-height:29px}
.btn-login{left:962px;top:11px;width:78px;height:29px;background:#e2e4e6;border:1px solid #c8cbcf;color:var(--ink);font-size:14px;text-align:center;line-height:27px}
.main-nav{top:72px;left:474px;font-size:14px;color:var(--muted)}
.main-nav a{text-decoration:none;color:inherit;position:absolute;white-space:nowrap}
.main-nav a.active{color:var(--sky)}

/* hero */
.hero{top:120px;left:0;width:1200px;height:655px;background:linear-gradient(120deg,#4c5e6c 0%,#3c4d5b 45%,#33434f 100%)}
.hero-title{left:160px;top:70px;color:var(--white);font-weight:300;font-size:56px;white-space:nowrap}
.hero-title strong{color:var(--sky);font-weight:700;font-size:62px}
.hero-text{left:162px;top:152px;width:870px;color:#e8edf1;font-size:20px;line-height:30px}
.btn-outline{border:2px solid var(--white);color:var(--white);text-align:center;font-size:19px}
.hero-more{left:490px;top:243px;width:191px;height:51px;line-height:47px}
.sell-title{left:0;top:352px;width:1200px;text-align:center;color:var(--white);font-weight:700;font-size:38px}
.hero-rule{left:0;top:425px;width:1200px;height:1px;background:rgba(255,255,255,.35)}
.field{height:38px;background:var(--field);border:1px solid #cfd5da;font-size:14px;color:#8d959c;padding:0 8px;line-height:36px}
.btn-submit{background:var(--sky-dark);color:var(--white);font-weight:700;font-size:19px;text-align:center;line-height:38px;height:38px;border:1px solid #8fd0f5}

/* steps */
.steps{top:775px;left:0;width:1200px;height:489px;background:var(--white)}
.step-label{font-size:21px;font-weight:600;color:#4a525a;line-height:26px}
.step-circle{width:126px;height:126px;border-radius:50%;display:flex;align-items:center;justify-content:center}
.step-circle.dark{background:var(--slate)}
.step-circle.light{background:var(--sky)}

/* we buy */
.house-photo{top:1264px;left:0;width:1200px;height:557px;background:linear-gradient(180deg,#5b8fd6 0%,#86aee0 30%,#9a9486 52%,#6f7d4a 72%,#4f7a35 100%)}
.buy-panel{left:490px;top:1351px;width:601px;height:423px;background:rgba(35,42,48,.82);color:var(--white);text-align:right;padding:0 54px 0 40px}
.buy-panel h2{font-size:34px;font-weight:700;margin-top:44px}
.buy-panel h3{font-size:30px;font-weight:400;margin-top:20px}
.buy-panel p{font-size:18px;line-height:27px;margin-top:22px;font-weight:300;margin-left:54px}
.buy-more{right:54px;bottom:40px;width:160px;height:42px;line-height:38px;font-size:18px}

/* features */
.features{top:1821px;left:0;width:1200px;height:605px;background:var(--white)}
.features h2{left:160px;top:125px;font-size:31px;font-weight:400;color:#454d55}
.features p{left:160px;top:188px;width:510px;font-size:18px;line-height:26px;color:var(--muted);font-weight:300}
.feature-list{left:160px;top:293px;list-style:none;font-size:18px;color:var(--muted);font-weight:300}
.feature-list li{height:38px;line-height:38px;padding-left:28px;position:relative}
.feature-list li::before{content:"";position:absolute;left:2px;top:14px;width:12px;height:12px;border-radius:50%;background:var(--slate)}
.feature-art{left:680px;top:1919px;width:520px;height:381px;background:linear-gradient(135deg,rgba(92,185,239,.18),rgba(61,75,88,.12))}

/* clients */
.clients{top:2426px;left:0;width:1200px;height:557px;background:linear-gradient(180deg,#2b3238 0%,#22282e 50%,#1b2025 100%)}
.clients h2{left:0;top:88px;width:1200px;text-align:center;color:var(--white);font-weight:700;font-size:36px}
.quote-text{left:240px;top:214px;width:720px;text-align:center;color:#e5e9ec;font-size:20px;line-height:30px;font-weight:300}
.quote-mark{font-family:Georgia,serif;font-size:110px;color:#d9dde0;line-height:1}
.avatar{left:543px;top:343px;width:116px;height:116px;border-radius:50%;border:5px solid var(--white);background:radial-gradient(circle at 50% 45%,#c9d7e2,#7f9db4)}
.client-name{left:0;top:476px;width:1200px;text-align:center;color:var(--white);font-size:19px}

/* footer */
.site-footer{top:2983px;left:0;width:1200px;height:357px;background:var(--footer);color:var(--white)}
.skyline{left:0;top:234px;width:1200px;height:123px;background:linear-gradient(180deg,rgba(255,255,255,0),rgba(255,255,255,.08))}
.footer-rule{left:0;top:96px;width:1200px;height:1px;background:var(--footer-line)}
.footer-h{top:56px;font-size:24px;font-weight:600}
.footer-about{left:162px;top:110px;width:230px;font-size:13px;line-height:16px}
.footer-nav{left:565px;top:111px;list-style:none;font-size:13px;line-height:23.5px}
.footer-social{left:888px;top:115px}
.footer-social span{background:var(--white);width:22px;height:22px}
.footer-brand{left:888px;top:163px;display:flex;align-items:center;gap:6px}
.footer-brand .brand-square{width:14px;height:14px}
.footer-brand .brand-name{font-size:12px;color:var(--white)}
.copyright{left:888px;top:204px;font-size:12px;line-height:15px}
</style>
</head>
<body>

<header class="site-header abs">
  <div class="brand abs"><span class="brand-square"></span><span class="brand-name">TOVIN TAKES HOMES</span></div>
  <div class="topbar-phone abs">
    <span class="phone-badge">
      <svg width="18" height="18" viewBox="0 0 24 24"><path d="M6.6 10.8a15 15 0 0 0 6.6 6.6l2.2-2.2c.3-.3.7-.4 1-.2 1.1.4 2.3.6 3.6.6.6 0 1 .4 1 1V20c0 .6-.4 1-1 1A17 17 0 0 1 3 4c0-.6.4-1 1-1h3.5c.6 0 1 .4 1 1 0 1.3.2 2.5.6 3.6.1.3 0 .7-.2 1z" fill="#fff"/></svg>
    </span>
    (555) 481-7720
  </div>
  <div class="social topbar-social abs"><span></span><span></span><span></span><span></span><span></span></div>
  <div class="btn-signup abs">Sign Up</div>
  <div class="btn-login abs">Log in</div>
  <nav class="main-nav abs">
    <a class="active" style="left:0">Home</a>
    <a style="left:74px">Sell My House</a>
    <a style="left:194px">Recent Projects</a>
    <a style="left:327px">How it Works</a>
    <a style="left:441px">About</a>
    <a style="left:512px">Contact</a>
  </nav>
</header>

<section class="hero abs" role="img" aria-label="Dim interior of a kitchen behind a slate blue overlay">
  <h1 class="hero-title abs">Welcome to <strong>TOVIN TAKES HOMES</strong></h1>
  <p class="hero-text abs">This is our sample version of Lorem Ipsum. Proin gravida nibh vel velit auctor alique Aenean sollicitudi orem quis bibendum auctor, nisi elit</p>
  <div class="btn-outline hero-more abs">Read More</div>
  <h2 class="sell-title abs">SELL YOUR HOUSE &#9662;</h2>
  <div class="hero-rule abs"></div>
  <div class="field abs" style="left:162px;top:477px;width:272px">First Name</div>
  <div class="field abs" style="left:459px;top:477px;width:280px">Last Name</div>
  <div class="field abs" style="left:766px;top:477px;width:271px">Phone</div>
  <div class="field abs" style="left:162px;top:546px;width:314px">Email</div>
  <div class="field abs" style="left:501px;top:546px;width:405px">Property Address</div>
  <div class="btn-submit abs" style="left:933px;top:546px;width:104px">Submit</div>
</section>

<section class="steps abs">
  <div class="step-label abs" style="left:160px;top:124px">1. Fill In the Form</div>
  <div class="step-label abs" style="left:621px;top:124px">3. Find a Solution</div>
  <div class="step-label abs" style="left:346px;top:339px;width:260px;text-align:center">2. Get a Call within<br>24 hours</div>
  <div class="step-label abs" style="left:816px;top:327px;width:260px;text-align:center">4. Go on with<br>Your Life</div>

  <svg class="abs" style="left:0;top:0" width="1200" height="489" viewBox="0 0 1200 489">
    <g fill="none" stroke="#9aa1a8" stroke-width="1.5" stroke-dasharray="5 4">
      <path d="M290 170 Q360 120 440 172"/>
      <path d="M760 170 Q830 120 905 172"/>
      <path d="M510 306 Q590 356 675 306"/>
    </g>
    <g fill="none" stroke="#9aa1a8" stroke-width="1.5">
      <path d="M432 162 l9 10 -13 3"/>
      <path d="M897 162 l9 10 -13 3"/>
      <path d="M665 300 l11 6 -10 8"/>
    </g>
  </svg>

  <div class="step-circle dark abs" style="left:180px;top:179px">
    <svg width="56" height="56" viewBox="0 0 48 48" fill="none" stroke="#fff" stroke-width="3" stroke-linejoin="round"><rect x="9" y="9" width="28" height="33" rx="3"/><path d="M17 6h12v6H17z" fill="#3d4b58"/><path d="M20 34l3-8 14-14 5 5-14 14z"/></svg>
  </div>
  <div class="step-circle light abs" style="left:413px;top:179px">
    <svg width="54" height="54" viewBox="0 0 24 24" fill="none" stroke="#fff" stroke-width="1.6"><path d="M6.6 10.8a15 15 0 0 0 6.6 6.6l2.2-2.2c.3-.3.7-.4 1-.2 1.1.4 2.3.6 3.6.6.6 0 1 .4 1 1V20c0 .6-.4 1-1 1A17 17 0 0 1 3 4c0-.6.4-1 1-1h3.5c.6 0 1 .4 1 1 0 1.3.2 2.5.6 3.6.1.3 0 .7-.2 1z"/><path d="M20 4l-6 6M14 5v5h5"/></svg>
  </div>
  <div class="step-circle dark abs" style="left:649px;top:179px">
    <svg width="54" height="54" viewBox="0 0 48 48" fill="none" stroke="#fff" stroke-width="3" stroke-linejoin="round"><path d="M10 20h8a4 4 0 1 1 8 0h8v8a4 4 0 1 1 0 8v6H10v-8a4 4 0 1 0 0-8z" transform="rotate(-35 24 28)"/></svg>
  </div>
  <div class="step-circle light abs" style="left:883px;top:179px">
    <svg width="54" height="60" viewBox="0 0 48 54" fill="none" stroke="#fff" stroke-width="3" stroke-linejoin="round"><path d="M17 6h14l-5 9h-4z"/><path d="M20 15C8 22 5 34 8 42c2 6 8 8 16 8s14-2 16-8c3-8 0-20-12-27z"/><text x="24" y="42" font-family="Source Sans 3, sans-serif" font-size="18" font-weight="700" fill="#fff" stroke="none" text-anchor="middle">$</text></svg>
  </div>
</section>

<section class="house-photo abs" role="img" aria-label="Single-storey house with green front lawn under a blue sky">
</section>
<div class="buy-panel abs">
  <h2>WE BUY HOUSES</h2>
  <h3>I need to sell my House, and Fast!</h3>
  <p>This is our sample version of Lorem Ipsum. Proin gravida nibh vel velit auctor aliquet. Aenean sollicitudin, lorem quis bibendum auctor, nisi elit consequat ipsum, nec sagittis sem nibh id elit. Duis sed odio sit amet nibh vulputate cursus a sit amet mauris. Morbi.</p>
  <div class="btn-outline buy-more abs">Read More</div>
</div>

<section class="features abs">
  <h2 class="abs">Lorem Ipsum Proin gravida nibh</h2>
  <p class="abs">This is our sample version of Lorem Ipsum. Proin gravida nibh vel velit auctor aliquet. Aenean sollicitudin, lorem quis bibendum auctor, nisi elit consequat ipsum, nec</p>
  <ul class="feature-list abs">
    <li>We pay cash</li>
    <li>We pay regular closing costs</li>
    <li>We buy houses as is</li>
    <li>No unreasonable home buyer demands</li>
    <li>Fast closings so you can move out and move on</li>
  </ul>
</section>
<div class="feature-art abs" role="img" aria-label="Large brand emblem area in sky blue and slate"></div>

<section class="clients abs" role="img" aria-label="Handshake in front of a house at dusk, darkened">
  <h2 class="abs">OUR CLIENTS</h2>
  <div class="quote-mark abs" style="left:162px;top:168px">&#8220;</div>
  <p class="quote-text abs">Lorem Ipsum is simply dummy text of the printing and typesetting industry. Lorem Ipsum has been the industry's standard dummy text ever since the 1500s Lorem Ipsum is simply dummy text of the printing and typesetting industry.</p>
  <div class="quote-mark abs" style="left:962px;top:286px">&#8221;</div>
  <svg class="abs" style="left:322px;top:378px" width="24" height="40" viewBox="0 0 24 40"><path d="M20 4L6 20l14 16" fill="none" stroke="#fff" stroke-width="5"/></svg>
  <svg class="abs" style="left:862px;top:378px" width="24" height="40" viewBox="0 0 24 40"><path d="M4 4l14 16L4 36" fill="none" stroke="#fff" stroke-width="5"/></svg>
  <div class="avatar abs" role="img" aria-label="Client portrait"></div>
  <div class="client-name abs">Dara Quell</div>
</section>

<footer class="site-footer abs">
  <div class="skyline abs" role="img" aria-label="Faint city skyline silhouette"></div>
  <h3 class="footer-h abs" style="left:162px">About Us</h3>
  <h3 class="footer-h abs" style="left:563px">Navigations</h3>
  <h3 class="footer-h abs" style="left:888px">Join Us</h3>
  <div class="footer-rule abs"></div>
  <p class="footer-about abs">This is our sample version of Lorem Ipsum. Proin gravida nibh vel velit auctor aliquet. Aenean sollicitudin, lorem quis bibendum auctor, nisi elit consequat ipsum, nec sagittis sem nibh id elit. Duis sed odio sit amet nibh vulputate cursus a sit amet.</p>
  <ul class="footer-nav abs">
    <li>Home</li>
    <li>Sell My House</li>
    <li>Recent Projects</li>
    <li>How it Works</li>
    <li>About</li>
  </ul>
  <div class="social footer-social abs"><span></span><span></span><span></span><span></span><span></span></div>
  <div class="footer-brand abs"><span class="brand-square"></span><span class="brand-name">TOVIN TAKES HOMES</span></div>
  <p class="copyright abs">© 2014 Tovin Takes Homes<br>All Rights Reserved</p>
</footer>

</body>
</html>
```